DunePrince.Com Website Design

We need a logo with website designed for the domain duneprince.com. This is a domain that will be a tribute domain for the ruler of Saudi Arabia. For reference you can see how emirkhalidon.com looks and do something similar. The site will need to be easily updateable. We will be adding news and content regularly so it will need to be a very content friendly site. We may even use word-press as the site management tool. We've uploaded the site map in the pdf that's attached along with some images that you can use for the site. Design needs to be per the sitemap. Please feel free to edit the images I've uploaded also use stock images if required.

Industry/Entity Type

Domain

Number of Pages Required

5+ page

Requirements
Must have
• Design has to be per the sitemap attached.

```html
<!DOCTYPE html>
<html lang="en">
<head>
<meta charset="utf-8">
<title>DunePrince.Com</title>
<link href="https://fonts.googleapis.com/css2?family=Roboto:wght@400;500;700&family=Oswald:wght@400;500&display=swap" rel="stylesheet">
<style>
:root{
  --navy:#0c3b74;
  --navy-dark:#082c59;
  --cyan:#0bb3ec;
  --orange:#f26522;
  --band:#e4e4e4;
  --footer:#e9e9e9;
  --text:#222;
  --muted:#6d6d6d;
  --link:#1b4f8a;
  --white:#fff;
}
*{box-sizing:border-box;margin:0;padding:0}
html,body{width:1200px;height:2922px;overflow:hidden}
body{position:relative;font-family:"Roboto",Arial,sans-serif;color:var(--text);background:var(--white)}
.abs{position:absolute}
a{color:inherit;text-decoration:none}

/* header */
.site-header{left:0;top:0;width:1200px;height:66px;background:var(--navy)}
.brand{left:74px;top:10px;display:flex;align-items:center;gap:8px;color:var(--white)}
.brand-mark{width:40px;height:44px;background:var(--white)}
.brand-name{font:700 18px/1 "Roboto",sans-serif;color:var(--white);width:80px}
.main-nav{left:0;top:0;width:1200px;height:66px}
.main-nav a{position:absolute;top:18px;color:var(--white);font:500 14px/14px "Roboto",sans-serif;padding:8px 14px}
.main-nav a.active{background:var(--cyan)}
.search-icon{left:1104px;top:23px}

/* hero */
.hero{left:0;top:66px;width:1200px;height:600px;background:linear-gradient(100deg,#6a4a26 0%,#a37a45 30%,#d9cdb8 55%,#b6904f 80%,#7a5a2e 100%)}
.hero-arrow{width:42px;height:42px;background:rgba(0,0,0,.55);display:flex;align-items:center;justify-content:center}
.hero-caption{left:74px;top:364px;width:270px;height:302px;background:rgba(12,59,116,.92);border-top:5px solid var(--cyan);padding:22px 18px;color:var(--white)}
.hero-caption .date{font:500 13px "Roboto",sans-serif;margin-bottom:10px}
.hero-caption h2{font:700 18px/1.2 "Roboto",sans-serif;margin-bottom:20px}
.hero-caption p{font:400 13px/1.5 "Roboto",sans-serif;margin-bottom:18px}
.btn{display:inline-flex;align-items:center;gap:5px;background:var(--navy);color:var(--white);font:500 11px "Roboto",sans-serif;padding:8px 10px;text-transform:uppercase}
.btn-outline{border:1px solid var(--white);background:transparent}

/* content band */
.band{left:0;top:666px;width:1200px;height:634px;background:var(--band)}
.panel{background:var(--white)}
.panel-title{font:400 22px/1 "Oswald",sans-serif;text-transform:uppercase;letter-spacing:.3px}
.latest{left:74px;top:709px;width:244px;height:543px;background:#f2f2f2}
.latest .panel-title{background:var(--cyan);color:var(--white);padding:8px 10px;height:40px}
.news-item{padding:14px 10px 12px;border-bottom:1px solid #d5d5d5;margin:0 8px 0 0}
.news-item .date{font:400 11px "Roboto";color:#444}
.news-item h3{font:500 13px/1.3 "Roboto";margin:3px 0 8px}
.news-item p{font:400 13px/1.4 "Roboto";color:var(--muted);margin-bottom:10px}
.more{font:700 10px "Roboto";color:var(--link);text-transform:uppercase}
.view-all{left:0;bottom:0;width:244px;height:28px;background:#5a6b7b;color:var(--white);font:500 14px/28px "Roboto";text-align:center;text-transform:uppercase}
.main-story{left:325px;top:709px;width:550px;height:543px;padding:22px 28px}
.main-story .panel-title{color:var(--cyan);margin-bottom:18px}
.photo{display:block}
.main-story h3{font:500 14px "Roboto";margin:18px 0 8px}
.main-story p{font:400 13px/1.58 "Roboto";color:var(--muted);margin-bottom:10px}
.newsletter{left:884px;top:709px;width:242px;height:142px;background:var(--navy);padding:16px 18px;color:var(--white)}
.newsletter .panel-title{font-size:20px;margin-bottom:14px}
.field{width:206px;height:30px;background:var(--white);color:#333;font:400 12px/30px "Roboto";padding-left:8px;margin-bottom:8px}
.signup{width:206px;height:30px;background:var(--orange);color:var(--white);font:700 13px/30px "Roboto";text-align:center}
.topics{left:884px;top:861px;width:242px;height:187px}
.topics .panel-title{background:var(--cyan);color:var(--white);font-size:20px;padding:8px 10px;height:36px}
.topics ul{list-style:none;padding:12px 18px}
.topics li{font:400 13px/1.45 "Roboto";color:var(--link);padding-left:10px;position:relative;margin-bottom:10px}
.topics li:before{content:"";position:absolute;left:0;top:7px;width:4px;height:4px;border-radius:50%;background:var(--link)}
.quotes{left:884px;top:1058px;width:242px;height:194px;background:var(--cyan);color:var(--white);padding:0 10px}
.quotes .panel-title{font-size:20px;padding:8px 0 6px;border-bottom:2px solid rgba(255,255,255,.6)}
.quotes .qbox{background:#19c1f4;margin-top:6px;padding:8px 16px;text-align:center;font:400 15px/1.4 "Roboto"}
.qmark{font:700 22px/1 "Roboto";display:block}

/* projects */
.project-feature{left:74px;top:1348px;width:600px;height:450px;border:1px solid #ddd;padding:8px}
.project-feature h3{font:500 16px "Roboto";margin:18px 10px 10px}
.project-feature p{font:400 13px/1.6 "Roboto";color:var(--muted);margin:0 10px 12px}
.project-feature .btn{margin-left:10px}
.project-small{left:703px;top:1346px;width:423px;height:150px;border:1px solid #ddd;padding:8px;display:flex;gap:14px}
.project-small h3{font:500 14px "Roboto";margin:6px 0 4px}
.project-small p{font:400 13px/1.4 "Roboto";color:var(--muted);margin-bottom:8px}
.social-box{left:703px;top:1519px;width:423px;height:279px;border:6px solid var(--navy);background:var(--white);padding:8px}
.social-head{display:flex;align-items:center;gap:8px;padding:2px 4px 8px}
.social-head .sq{width:32px;height:32px;background:var(--navy)}
.social-head b{font:700 13px "Roboto";color:var(--link);display:block}
.like{display:inline-block;background:#4a66a0;color:var(--white);font:700 10px "Roboto";padding:2px 6px;margin-top:3px}
.fans{background:#eef0f5;border-top:1px solid #cfd3dc;padding:6px 8px;height:196px}
.fans .count{font:400 11px "Roboto";color:#333;margin-bottom:6px}
.fan-grid{display:grid;grid-template-columns:repeat(7,1fr);gap:6px 8px}
.fan{text-align:center;font:400 10px "Roboto";color:#555}
.fan i{display:block;height:50px;background:#dfe3ea;margin-bottom:3px}
.plugin{font:400 10px "Roboto";color:#555;padding:5px 4px}

/* video */
.video{left:74px;top:1847px;width:1052px;height:526px;background:linear-gradient(90deg,#2b2114 0%,#54452c 35%,#2c2a28 60%,#3a3a36 100%)}
.video-title{left:74px;top:2046px;width:1052px;text-align:center;color:var(--white)}
.video-title h2{font:400 33px/1 "Roboto";margin-bottom:4px}
.video-title p{font:400 21px "Roboto"}
.play{left:560px;top:2131px}

/* footer */
.footer-nav{left:0;top:2406px;width:1200px;height:41px;background:var(--cyan)}
.footer-nav a{position:absolute;top:13px;color:var(--white);font:400 13px/15px "Roboto";text-transform:uppercase}
.footer-social{left:952px;top:2411px;display:flex;gap:6px}
.footer-social i{width:30px;height:30px;border:2px solid var(--white);display:block}
.footer{left:0;top:2447px;width:1200px;height:417px;background:var(--footer)}
.fcol{top:2478px;width:330px}
.fcol a{display:block;font:400 13px "Roboto";color:var(--link);padding-left:9px;position:relative;margin-bottom:12px}
.fcol a:before{content:"";position:absolute;left:0;top:4px;border-left:4px solid var(--link);border-top:4px solid transparent;border-bottom:4px solid transparent}
.fcol p{font:400 12px/1.6 "Roboto";color:var(--muted);margin:-4px 0 12px 9px}
.footer-bottom{left:74px;top:2864px;width:1052px;height:58px;border-top:1px solid #ccc;display:flex;justify-content:space-between;align-items:center;font:400 12px "Roboto";color:#444;background:var(--footer)}
.footer-base{left:0;top:2864px;width:1200px;height:58px;background:var(--footer)}
</style>
</head>
<body>

<header class="site-header abs">
  <div class="brand abs"><span class="brand-mark"></span><span class="brand-name">DunePrince</span></div>
  <nav class="main-nav abs">
    <a class="active" href="#" style="left:296px">HOME</a>
    <a href="#" style="left:401px">NEWS</a>
    <a href="#" style="left:508px">BOUT</a>
    <a href="#" style="left:611px">CAREER</a>
    <a href="#" style="left:732px">FOUNDATIONS &amp; ACTIVITIES</a>
    <a href="#" style="left:993px">MEDIA</a>
  </nav>
  <svg class="search-icon abs" width="18" height="18" viewBox="0 0 18 18"><circle cx="7" cy="7" r="5.5" fill="none" stroke="#fff" stroke-width="2"/><line x1="11" y1="11" x2="16" y2="16" stroke="#fff" stroke-width="2"/></svg>
</header>

<section class="hero abs" role="img" aria-label="Photo of the prince seated at a conference desk in front of an ornate gold wall"></section>
<div class="hero-arrow abs" style="left:10px;top:344px"><svg width="12" height="14"><path d="M10 1 2 7l8 6z" fill="#fff"/></svg></div>
<div class="hero-arrow abs" style="left:1148px;top:344px"><svg width="12" height="14"><path d="M2 1l8 6-8 6z" fill="#fff"/></svg></div>
<div class="hero-caption abs">
  <div class="date">10.12.2016</div>
  <h2>Lorem ipsum dolor sit amet, consectetur adipiscing elit</h2>
  <p>Sed do eiusmod tempor incididunt ut labore et dolore magna aliqua. Ut enim ad minim veniam, quis nostrud exercitation ullamco laboris nisi ut aliquip ex ea commodo consequat.</p>
  <a class="btn btn-outline" href="#">Read more ▸</a>
</div>

<section class="band abs"></section>

<aside class="latest abs">
  <h2 class="panel-title">Latest News</h2>
  <div class="news-item"><div class="date">12.12.2016</div><h3>Lorem ipsum dolor sit amet, cons ectetur adipiscing elit</h3><p>Sed ut perspiciatis unde omnis iste natus error sit.</p><a class="more" href="#">Read more ▸</a></div>
  <div class="news-item"><div class="date">12.12.2016</div><h3>Lorem ipsum dolor sit amet, cons ectetur adipiscing elit</h3><p>Sed ut perspiciatis unde omnis iste natus error sit.</p><a class="more" href="#">Read more ▸</a></div>
  <div class="news-item" style="border:0"><div class="date">12.12.2016</div><h3>Lorem ipsum dolor sit amet, cons ectetur adipiscing elit</h3><p>Sed ut perspiciatis unde omnis iste natus error sit.</p><a class="more" href="#">Read more ▸</a></div>
  <a class="view-all abs" href="#">View All</a>
</aside>

<article class="main-story panel abs">
  <h2 class="panel-title">Main Story of the Week/Month</h2>
  <div class="photo" style="width:494px;height:210px;background:linear-gradient(90deg,#c9c2b8,#8d8077 50%,#3f5e8c)" role="img" aria-label="Portrait photo of the prince smiling in front of a patterned blue chair"></div>
  <h3>Lorem ipsum dolor sit amet, consectetur adipiscing elit</h3>
  <p>Sed ut perspiciatis unde omnis iste natus error sit voluptatem accusantium doloremque laudantium, totam rem aperiam, eaque ipsa quae ab illo inventore veritatis et quasi architecto beatae vitae dicta sunt explicabo. Nemo enim ipsam voluptatem quia voluptas sit aspernatur aut odit aut fugit, sed quia consequuntur magni dolores eos qui ratione voluptatem sequi nesciunt. Neque porro quisquam est, qui dolorem ipsum quia dolor sit amet, consectetur, adipisci velit, sed quia non numquam eius modi tempora incidunt ut labore et dolore magnam aliquam quaerat voluptatem.</p>
  <a class="btn" href="#">Read more ▸</a>
</article>

<div class="newsletter abs">
  <h2 class="panel-title">Newsletter Signup</h2>
  <div class="field">Enter your email address</div>
  <div class="signup">SIGNUP</div>
</div>

<div class="topics panel abs">
  <h2 class="panel-title">Popular Topics</h2>
  <ul><li>Lorem ipsum dolor sit amet</li><li>Nullam non nunc in turpis euismod tempor.</li><li>Sed pulvinar magna pretium lobortis pharetra.</li></ul>
</div>

<div class="quotes abs">
  <h2 class="panel-title">Quotes by the Prince</h2>
  <div class="qbox"><span class="qmark">“</span>Sed ut perspiciatis unde omnis iste natus error sit voluptatem accusantium doloremque laudantium, totam rem aperiam,<span class="qmark">”</span></div>
</div>

<article class="project-feature abs">
  <div style="width:582px;height:240px;background:linear-gradient(90deg,#7d6a48,#b9a98b 45%,#4e4336)" role="img" aria-label="Photo of the prince reading at a desk"></div>
  <h3>Projects of Prince Faris</h3>
  <p>Nemo enim ipsam voluptatem quia voluptas sit aspernatur aut odit aut fugit, sed quia consequuntur magni dolores eos qui ratione voluptatem sequi nesciunt. Neque porro quisquam est, qui dolorem ipsum quia dolor sit amet, consectetur, adipisci velit, sed quia non numquam eius modi tempora incidunt ut labore et dolore magnam aliquam quaerat voluptatem.</p>
  <a class="btn" href="#">Read more ▸</a>
</article>

<article class="project-small abs">
  <div style="flex:0 0 168px;height:126px;background:linear-gradient(90deg,#6b5a3e,#c9b79b 50%,#5d4a33)" role="img" aria-label="Photo of the prince seated at a formal meeting"></div>
  <div>
    <h3>Projects of Prince Faris</h3>
    <p>Lorem ipsum dolor sit amet, consectetur adipiscing elit, sed do eiusmod tempor incididunt</p>
    <a class="btn" href="#">Read more ▸</a>
  </div>
</article>

<div class="social-box abs">
  <div class="social-head"><span class="sq"></span><div><b>DunePrince</b><span class="like">Like</span></div></div>
  <div class="fans">
    <div class="count">934,610 people like DunePrince</div>
    <div class="fan-grid">
      <div class="fan"><i></i>Jay</div><div class="fan"><i></i>Josh</div><div class="fan"><i></i>Richard</div><div class="fan"><i></i>Luis</div><div class="fan"><i></i>William</div><div class="fan"><i></i>Jay</div><div class="fan"><i></i>Josh</div>
      <div class="fan"><i></i>Jesse</div><div class="fan"><i></i>Judie</div><div class="fan"><i></i>Josh</div><div class="fan"><i></i>Richard</div><div class="fan"><i></i>Luis</div><div class="fan"><i></i>Jesse</div><div class="fan"><i></i>Judie</div>
    </div>
  </div>
  <div class="plugin">Social plugin</div>
</div>

<section class="video abs" role="img" aria-label="Video still of the prince standing at a desk in an office with flags and curtains"></section>
<div class="video-title abs"><h2>Video Profile of Prince Faris’s</h2><p>Accomplishments</p></div>
<svg class="play abs" width="80" height="80" viewBox="0 0 80 80"><circle cx="40" cy="40" r="36" fill="none" stroke="#fff" stroke-width="5"/><path d="M32 24 56 40 32 56z" fill="#fff"/></svg>

<nav class="footer-nav abs">
  <a href="#" style="left:72px">Home</a>
  <a href="#" style="left:162px">News</a>
  <a href="#" style="left:251px">About</a>
  <a href="#" style="left:345px">Career</a>
  <a href="#" style="left:446px">Foundations &amp; Activities</a>
  <a href="#" style="left:684px">Media</a>
</nav>
<div class="footer-social abs"><i></i><i></i><i></i><i></i><i></i></div>

<footer class="footer abs"></footer>
<div class="fcol abs" style="left:74px">
  <a href="#">Information</a>
  <a href="#">Prince Faris bin Nasir</a>
  <p>Lorem ipsum dolor sit amet, consectetur adipiscing elit, sed do eiusmod tempor incididunt ut labore et dolore magna aliqua.</p>
  <p>Ut enim ad minim veniam, quis nostrud exercitation ullamco laboris nisi ut aliquip ex ea commodo consequat.</p>
  <a href="#">Emir Khalidon</a>
  <p>Lorem ipsum dolor sit amet, consectetur adipiscing elit, sed do eiusmod tempor incididunt ut labore et dolore magna aliqua.</p>
  <a href="#">About Emir Khalidon</a>
  <a href="#">About Zaharia</a>
</div>
<div class="fcol abs" style="left:432px">
  <a href="#">About Us</a>
  <p>Lorem ipsum dolor sit amet, consectetur adipiscing elit, sed do eiusmod tempor incididunt ut labore et dolore magna aliqua.</p>
  <a href="#">Contribution</a>
  <p>Lorem ipsum dolor sit amet, consectetur adipiscing elit, sed do eiusmod tempor incididunt ut labore et dolore magna aliqua.</p>
  <a href="#">“ The Sheikh ”</a>
  <a href="#">Awards and Achievements</a>
  <a href="#">Horizon Plan</a>
  <a href="#">Kingdom of Qaradan</a>
  <p>Lorem ipsum dolor sit amet, consectetur adipiscing elit, sed do eiusmod tempor incididunt ut labore et dolore magna aliqua.</p>
</div>
<div class="fcol abs" style="left:793px">
  <a href="#">Quotes</a><a href="#">Speeches</a><a href="#">Foundations</a><a href="#">Thoughts</a><a href="#">Interviews</a><a href="#">Articles</a><a href="#">Gallery</a>
</div>

<div class="footer-base abs"></div>
<div class="footer-bottom abs">
  <span>© 2016 DunePrince. All Rights Reserved.</span>
  <span>Legal Agreements &nbsp;|&nbsp; Terms of use &nbsp;|&nbsp; Privacy policy</span>
</div>

</body>
</html>
```